Spinning Wheel: Spin & Win

We are looking to design a large sticker cover for a spinning wheel (please see attached reference)

Wheel diameter: 120 cm (1.2meters)

Divided into 8 sections:
1- Free Meal
2- Talvor Gift Card
3- Haircut or Blowdry
4- Talvor Gift Card
5- Merchandise
6- Talvor Gift Card
7- Meal voucher
8- Talvor Gift Card

Text in the center:
Buy for 200 AED to Spin & Win!
(Spin & Win should be the most dominant visually)

Font: Something classy and elegant (maybe cursive but easily read)

Colors: Khaki - All shades of brown and dark brown (note: the wheel structure is made of wood that is dark brown)

Feel: Wood and Old Paper

Target Market(s)

Upper Class

Industry/Entity Type

Graphic Design

Font styles to use
Decorative
Script

Requirements
Should not have
• Flashy colors

```html
<!DOCTYPE html>
<html lang="en">
<head>
<meta charset="utf-8">
<title>Spin &amp; Win Wheel Cover</title>
<link rel="stylesheet" href="https://fonts.googleapis.com/css2?family=Cormorant+Garamond:ital,wght@1,700&family=Great+Vibes&display=swap">
<style>
  :root {
    --khaki: #cdb785;
    --walnut: #8a5a2e;
    --espresso: #4e2f18;
    --ink: #2b1a0d;
    --cream: #f3e6c4;
    --paper: #efe2bf;
    --rim: #3a2313;
    --page: #ffffff;
    --art-on-light: #6b4a2b;
    --art-on-dark: #d9c293;
  }
  html, body {
    margin: 0;
    padding: 0;
    width: 1200px;
    height: 1200px;
    overflow: hidden;
    background: var(--page);
  }
  .canvas { width: 1200px; height: 1200px; display: block; }
  .slice-khaki { fill: var(--khaki); }
  .slice-walnut { fill: var(--walnut); }
  .slice-espresso { fill: var(--espresso); }
  .divider { stroke: var(--rim); stroke-width: 5; }
  .rim { fill: none; stroke: var(--rim); stroke-width: 16; }
  .prize-label {
    font-family: "Cormorant Garamond", serif;
    font-style: italic;
    font-weight: 700;
    font-size: 40px;
    fill: var(--ink);
    text-anchor: middle;
  }
  .on-dark .prize-label { fill: var(--cream); }
  .brand-name {
    font-family: "Cormorant Garamond", serif;
    font-style: italic;
    font-weight: 700;
    font-size: 34px;
    fill: var(--ink);
  }
  .brand-square { fill: var(--ink); }
  .prize-art { fill: var(--art-on-light); }
  .on-dark .prize-art { fill: var(--art-on-dark); }
  .hub-disc { fill: var(--paper); stroke: var(--rim); stroke-width: 8; }
  .hub-crown { fill: var(--espresso); }
  .hub-lead {
    font-family: "Cormorant Garamond", serif;
    font-style: italic;
    font-weight: 700;
    font-size: 21px;
    fill: var(--art-on-light);
    text-anchor: middle;
  }
  .hub-big {
    font-family: "Great Vibes", cursive;
    font-size: 72px;
    fill: var(--espresso);
    text-anchor: middle;
  }
</style>
</head>
<body>
<svg class="canvas" viewBox="0 0 1200 1200" xmlns="http://www.w3.org/2000/svg">
  <g class="wheel-slices">
    <path class="slice-espresso" d="M600 600 L600 80 A520 520 0 0 1 967.7 232.3 Z"/>
    <path class="slice-khaki" d="M600 600 L967.7 232.3 A520 520 0 0 1 1120 600 Z"/>
    <path class="slice-espresso" d="M600 600 L1120 600 A520 520 0 0 1 967.7 967.7 Z"/>
    <path class="slice-khaki" d="M600 600 L967.7 967.7 A520 520 0 0 1 600 1120 Z"/>
    <path class="slice-walnut" d="M600 600 L600 1120 A520 520 0 0 1 232.3 967.7 Z"/>
    <path class="slice-khaki" d="M600 600 L232.3 967.7 A520 520 0 0 1 80 600 Z"/>
    <path class="slice-walnut" d="M600 600 L80 600 A520 520 0 0 1 232.3 232.3 Z"/>
    <path class="slice-khaki" d="M600 600 L232.3 232.3 A520 520 0 0 1 600 80 Z"/>
  </g>

  <g class="wheel-dividers">
    <line class="divider" x1="600" y1="600" x2="600" y2="80"/>
    <line class="divider" x1="600" y1="600" x2="967.7" y2="232.3"/>
    <line class="divider" x1="600" y1="600" x2="1120" y2="600"/>
    <line class="divider" x1="600" y1="600" x2="967.7" y2="967.7"/>
    <line class="divider" x1="600" y1="600" x2="600" y2="1120"/>
    <line class="divider" x1="600" y1="600" x2="232.3" y2="967.7"/>
    <line class="divider" x1="600" y1="600" x2="80" y2="600"/>
    <line class="divider" x1="600" y1="600" x2="232.3" y2="232.3"/>
  </g>

  <g class="prize free-meal on-dark" transform="rotate(22.5 600 600)">
    <rect class="prize-art" x="548" y="150" width="104" height="96" rx="14" role="img" aria-label="Line drawing of a covered serving dish with fork and knife"/>
    <text class="prize-label" x="600" y="296">Free Meal</text>
  </g>

  <g class="prize gift-card" transform="rotate(67.5 600 600)">
    <rect class="brand-square" x="538" y="150" width="22" height="22"/>
    <text class="brand-name" x="568" y="172">Talvor</text>
    <text class="prize-label" x="600" y="238">Talvor Gift</text>
    <text class="prize-label" x="600" y="280">Card</text>
  </g>

  <g class="prize meal-voucher on-dark" transform="rotate(112.5 600 600)">
    <text class="prize-label" x="600" y="170">Meal voucher</text>
    <rect class="prize-art" x="530" y="196" width="140" height="90" rx="8" role="img" aria-label="Drawing of a meal voucher ticket"/>
  </g>

  <g class="prize gift-card" transform="rotate(157.5 600 600)">
    <text class="prize-label" x="600" y="170">Talvor Gift</text>
    <text class="prize-label" x="600" y="212">Card</text>
    <rect class="brand-square" x="538" y="248" width="22" height="22"/>
    <text class="brand-name" x="568" y="270">Talvor</text>
  </g>

  <g class="prize haircut on-dark" transform="rotate(202.5 600 600)">
    <text class="prize-label" x="600" y="168">Haircut</text>
    <text class="prize-label" x="600" y="206">or Blowdry</text>
    <circle class="prize-art" cx="600" cy="268" r="46" role="img" aria-label="Icon of scissors and a comb inside a circle"/>
  </g>

  <g class="prize gift-card" transform="rotate(247.5 600 600)">
    <text class="prize-label" x="600" y="170">Talvor Gift</text>
    <text class="prize-label" x="600" y="212">Card</text>
    <rect class="brand-square" x="538" y="248" width="22" height="22"/>
    <text class="brand-name" x="568" y="270">Talvor</text>
  </g>

  <g class="prize merchandise on-dark" transform="rotate(292.5 600 600)">
    <rect class="prize-art" x="548" y="150" width="104" height="96" rx="18" role="img" aria-label="Drawing of branded merchandise, a cap and a mug"/>
    <text class="prize-label" x="600" y="296">Merchandise</text>
  </g>

  <g class="prize gift-card" transform="rotate(337.5 600 600)">
    <rect class="brand-square" x="538" y="150" width="22" height="22"/>
    <text class="brand-name" x="568" y="172">Talvor</text>
    <text class="prize-label" x="600" y="238">Talvor Gift</text>
    <text class="prize-label" x="600" y="280">Card</text>
  </g>

  <circle class="rim" cx="600" cy="600" r="522"/>

  <g class="hub">
    <circle class="hub-disc" cx="600" cy="600" r="140"/>
    <path class="hub-crown" d="M578 512 L582 492 L592 503 L600 488 L608 503 L618 492 L622 512 Z" role="img" aria-label="Small crown ornament"/>
    <text class="hub-lead" x="600" y="542">Buy for 200 AED to</text>
    <text class="hub-big" x="600" y="608">Spin &amp;</text>
    <text class="hub-big" x="600" y="674">Win!</text>
  </g>
</svg>
</body>
</html>
```